Property Development company needs a business card design

i need a business card design for my company. we are a very small property developer specialising in land subdivisions in geelong Australia.

I would like to see a splash of brown yellow brown that is my favorite football team colors. (Pelmont) Its needs to be not offensive and slighlty subtle or mysterious or cheeky. I would like a white background with black writing.

Company is Varnel Property Developments. We dont have a logo - maybe a picture of a house /fence / gate / road could or couldnt work? I dont really know.

```html
<!DOCTYPE html>
<html lang="en">
<head>
<meta charset="utf-8">
<title>Varnel Property Developments – Business Card</title>
<link href="https://fonts.googleapis.com/css2?family=Roboto+Condensed:wght@400&display=swap" rel="stylesheet">
<style>
  :root {
    --backdrop: #3b3b3b;
    --card-white: #f4f4f4;
    --band-black: #0c0c0c;
    --band-brown: #5e2a0c;
    --band-yellow: #e8b931;
    --ink: #111111;
    --brand-brown: #5a260b;
    --rule-grey: #8a8a8a;
  }
  html, body {
    margin: 0;
    padding: 0;
    width: 1200px;
    height: 1000px;
    overflow: hidden;
    background: var(--backdrop);
  }
  .canvas {
    position: relative;
    width: 1200px;
    height: 1000px;
  }
  .business-card {
    position: absolute;
    left: 150px;
    top: 240px;
    width: 900px;
    height: 520px;
    background: var(--card-white);
    overflow: hidden;
    box-shadow: 0 12px 30px rgba(0,0,0,0.45);
  }
  .card-bands {
    position: absolute;
    inset: 0;
    width: 900px;
    height: 520px;
  }
  .band-black { fill: var(--band-black); }
  .band-brown { fill: var(--band-brown); }
  .band-yellow { fill: var(--band-yellow); }

  .company-name {
    position: absolute;
    left: 120px;
    top: 200px;
    margin: 0;
    font-family: "Roboto Condensed", "Arial Narrow", sans-serif;
    font-weight: 400;
    font-size: 60px;
    line-height: 1;
    color: var(--brand-brown);
    letter-spacing: 0.5px;
  }
  .contact-row {
    position: absolute;
    left: 122px;
    top: 318px;
    display: flex;
    align-items: center;
    gap: 18px;
    font-family: "Roboto Condensed", "Arial Narrow", sans-serif;
    font-weight: 400;
    font-size: 30px;
    color: var(--ink);
  }
  .contact-item {
    display: flex;
    align-items: center;
    gap: 8px;
  }
  .contact-icon {
    width: 36px;
    height: 30px;
    flex: none;
  }
  .contact-divider {
    width: 2px;
    height: 42px;
    background: var(--rule-grey);
  }
</style>
</head>
<body>
<div class="canvas">
  <section class="business-card" aria-label="Varnel Property Developments business card">
    <svg class="card-bands" viewBox="0 0 900 520" aria-hidden="true">
      <!-- top-left corner bands -->
      <polygon class="band-yellow" points="0,0 900,0 900,8 0,158"/>
      <polygon class="band-brown" points="0,0 760,0 0,122"/>
      <polygon class="band-black" points="0,0 540,0 0,86"/>
      <!-- bottom-right corner bands -->
      <polygon class="band-yellow" points="130,520 900,388 900,520"/>
      <polygon class="band-brown" points="300,520 900,418 900,520"/>
      <polygon class="band-black" points="480,520 900,448 900,520"/>
    </svg>

    <h1 class="company-name">Varnel Property Developments</h1>

    <div class="contact-row">
      <div class="contact-item contact-email">
        <svg class="contact-icon" viewBox="0 0 36 30" aria-hidden="true">
          <rect x="2" y="5" width="32" height="22" fill="none" stroke="#111" stroke-width="2"/>
          <polyline points="2,5 18,18 34,5" fill="none" stroke="#111" stroke-width="2"/>
          <polyline points="2,27 14,15" fill="none" stroke="#111" stroke-width="1.5"/>
          <polyline points="34,27 22,15" fill="none" stroke="#111" stroke-width="1.5"/>
        </svg>
        <span>info@varnelproperty.com</span>
      </div>
      <span class="contact-divider" aria-hidden="true"></span>
      <div class="contact-item contact-phone">
        <svg class="contact-icon" viewBox="0 0 30 30" aria-hidden="true">
          <path d="M7 2 L12 2 L14 9 L10.5 11.5 C12 15.5 14.5 18 18.5 19.5 L21 16 L28 18 L28 23 C28 26 25 28 22 27.5 C12 25.5 4.5 18 2.5 8 C2 5 4 2 7 2 Z" fill="#111"/>
        </svg>
        <span>0800.555.0142</span>
      </div>
    </div>
  </section>
</div>
</body>
</html>
```